10-slide template for ESG report for small businesses in Europe

Presentation goal: for owners of small businesses in Europe to report on their ESG metrics to various internal and external stakeholders, but typically used as part of their annual (financial) report.
Who is the target audience: small business owners/managers in Europe (these are business people, but not very corporate)
How is it going to be used: this template will be used to generate PDF reports automatically based on various inputs. The final output will not be reviewed or corrected by a human; hence we need to make sure that the template is flexible enough to be used for a variety of different inputs (specifically, in some cases there will be no input, and in some cases there will be many characters).
Desired look and feel: following VelloQuist brand style guide (attached). It's for business use so it's somewhat formal, but I do not want it to come across too corporate, so it's OK if there are playful elements.
What is the catch: the fact the template will need to be flexible enough to allow for the report to still look OK even if a certain fields do not have a value (specifically, as mentioned earlier there are some text fields that are likely going to be empty, but could have up to 1000 characters of text).
Illustrations: to keep it generic and relevant for a variety of businesses across all of Europe it's probably better to use simple flat style illustrations instead of photos. I've been using https://brindlecove.example/ to create those (see example attached) but I'm open to anything.
Lastly: please note that I'm very open to changing the position and size of all copy, tables, illustrations etc. I know I'm a terrible designer - that's why I'm here ;-)
Look and feel
Each slider illustrates characteristics of the customer's brand and the style your logo design should communicate.

```html
<!DOCTYPE html>
<html lang="en">
<head>
<meta charset="utf-8">
<title>Environmental, Social, and Governance Report – Consulting Business</title>
<link rel="stylesheet" href="https://fonts.googleapis.com/css2?family=Lexend:wght@500;600;700&family=Roboto:wght@400;500;700&display=swap">
<style>
  :root {
    --navy: #1b2963;
    --navy-deep: #16214f;
    --green: #8dc21f;
    --green-mid: #5e9c2b;
    --green-text: #8cbf26;
    --ink: #3b3f4a;
    --muted: #6c717c;
    --page: #f2f5f1;
    --cell: #e9ecf5;
    --line: #d7dbe6;
    --cover-bg: #f5f6f8;
  }
  * { box-sizing: border-box; margin: 0; padding: 0; }
  html, body { width: 1200px; height: 4051px; overflow: hidden; }
  body {
    background: var(--page);
    font-family: "Roboto", Arial, sans-serif;
    color: var(--ink);
  }
  .deck {
    display: flex; flex-direction: column; align-items: center;
    gap: 67px; padding-top: 87px;
  }
  .slide {
    position: relative; width: 1048px; height: 590px;
    background: #fff; overflow: hidden;
    box-shadow: 0 6px 18px rgba(27, 41, 99, 0.12);
  }
  .abs { position: absolute; }

  /* brand mark */
  .client-mark {
    font-family: "Roboto", Arial, sans-serif; font-weight: 500;
    color: var(--navy); font-size: 40px; letter-spacing: 0.5px; line-height: 1;
  }

  /* cover */
  .cover .client-mark { left: 60px; top: 26px; }
  .date-pill {
    left: 60px; top: 186px; height: 31px; padding: 0 14px 0 4px;
    display: flex; align-items: center; gap: 10px;
    background: var(--green); border-radius: 16px;
    color: #fff; font-size: 13px; font-weight: 500;
  }
  .date-pill .dot {
    width: 23px; height: 23px; border-radius: 50%; background: #fff;
    display: flex; align-items: center; justify-content: center;
  }
  .cover-title {
    left: 60px; top: 244px; width: 380px;
    font-family: "Lexend", sans-serif; font-weight: 700;
    font-size: 31px; line-height: 38px; color: var(--navy-deep);
  }
  .cover-sub { left: 60px; top: 378px; font-size: 23px; color: var(--navy-deep); }
  .cover-art { left: 0; top: 0; }
  .cover-illus { left: 560px; top: 140px; width: 400px; height: 330px; }

  /* slide header */
  .head-tab {
    left: 0; top: 0; width: 643px; height: 79px;
    background: var(--navy); border-bottom-right-radius: 70px;
    border-left: 4px solid var(--green);
    display: flex; align-items: center; padding-left: 56px;
    font-family: "Lexend", sans-serif; font-weight: 600;
    font-size: 30px; color: #fff;
  }
  .head-tab.small { font-size: 25px; }
  .slide .head-mark { right: 57px; top: 19px; }

  /* footer */
  .foot {
    left: 60px; right: 0; top: 527px; height: 43px;
    border-radius: 22px 0 0 22px;
    background: linear-gradient(90deg, var(--navy) 0%, var(--navy) 46%, var(--green-mid) 78%, var(--green) 100%);
    color: #fff; font-size: 12.5px; font-weight: 500;
  }
  .foot .cal {
    position: absolute; left: 8px; top: 6px; width: 31px; height: 31px;
    border-radius: 50%; background: #fff;
    display: flex; align-items: center; justify-content: center;
  }
  .foot span { position: absolute; top: 14px; }
  .foot .f-date { left: 55px; }
  .foot .f-title { left: 181px; }
  .foot .f-biz { left: 503px; }
  .foot .f-page { left: 849px; letter-spacing: 1px; }

  /* body copy */
  .copy {
    font-size: 13px; line-height: 20.5px; text-align: justify; color: var(--ink);
  }
  .copy p + p { margin-top: 10px; }
  .copy.fine { font-size: 11.5px; line-height: 19px; }
  .greet {
    font-size: 22px; color: var(--green-text); font-weight: 500;
  }
  .section-label { font-size: 16px; color: var(--green-text); font-weight: 500; }
  .sign { font-size: 15px; font-weight: 700; color: var(--navy-deep); }
  .sign small { font-size: 12px; font-weight: 500; }

  .bullets { list-style: none; }
  .bullets li {
    position: relative; padding-left: 28px;
    font-size: 11.5px; line-height: 19px; text-align: justify; color: var(--ink);
  }
  .bullets li + li { margin-top: 10px; }
  .bullets li svg { position: absolute; left: 0; top: 3px; }

  .badges {
    left: 539px; top: 344px; width: 184px;
    display: grid; grid-template-columns: 86px 86px; gap: 12px 12px;
  }
  .badge {
    height: 50px; background: #fff; border-radius: 6px;
    box-shadow: 0 2px 8px rgba(27,41,99,0.14);
    display: flex; align-items: center; justify-content: center;
  }
  .badge i { display: block; width: 44px; height: 22px; border-radius: 4px; }

  /* tables */
  .scope-table { left: 60px; top: 279px; border-collapse: separate; border-spacing: 0 3px; }
  .scope-table th, .scope-table td { height: 35px; font-size: 14px; text-align: left; }
  .scope-table th {
    width: 120px; padding-left: 20px; background: var(--cell);
    color: var(--navy-deep); font-weight: 500; border-radius: 4px 0 0 4px;
  }
  .scope-table td {
    width: 122px; padding-left: 18px; background: #fff; color: var(--ink);
    border: 1px solid var(--line); font-size: 12.5px; border-radius: 0 4px 4px 0;
  }
  .scope-note { font-size: 9.5px; line-height: 16px; color: var(--muted); text-align: justify; }

  .metric-table { left: 60px; top: 295px; border-collapse: separate; border-spacing: 0 3px; }
  .metric-table th, .metric-table td { height: 29px; font-size: 11px; text-align: left; }
  .metric-table th {
    width: 324px; padding-left: 16px; background: var(--cell);
    color: var(--navy-deep); font-weight: 500;
  }
  .metric-table td {
    width: 54px; padding-left: 22px; border: 1px solid var(--line); border-left: 4px solid #fff;
    color: var(--ink); font-size: 12px;
  }

  /* stat circles */
  .stat { display: flex; align-items: center; gap: 16px; }
  .ring {
    width: 72px; height: 72px; border-radius: 50%; flex: none;
    background: conic-gradient(var(--green) 0 100%);
    padding: 5px;
  }
  .ring b {
    display: flex; align-items: center; justify-content: center;
    width: 100%; height: 100%; border-radius: 50%; background: #fff;
    font-size: 17px; font-weight: 700; color: var(--navy-deep);
  }
  .stat p { font-size: 14.5px; line-height: 21px; color: var(--ink); }

  .illus {
    border-radius: 28px;
    background: linear-gradient(135deg, #e6ecfb 0%, #eef1fb 55%, #fbefcb 100%);
  }
</style>
</head>
<body>
<main class="deck">

  <!-- Cover -->
  <section class="slide cover">
    <svg class="abs cover-art" width="1048" height="590" viewBox="0 0 1048 590" aria-hidden="true">
      <defs>
        <linearGradient id="bandGrad" x1="0" y1="0" x2="0" y2="1">
          <stop offset="0" stop-color="#6ea52a"/>
          <stop offset="0.45" stop-color="#2f5a4a"/>
          <stop offset="1" stop-color="#1b2963"/>
        </linearGradient>
      </defs>
      <path d="M662 0 L1048 0 L1048 590 L716 590 L528 446 Q482 408 502 358 Z" fill="var(--cover-bg)"/>
      <path d="M612 -20 L446 356 Q418 428 478 474 L650 612" fill="none" stroke="url(#bandGrad)" stroke-width="88" stroke-linejoin="round"/>
    </svg>
    <div class="abs client-mark">[client logo]</div>
    <div class="abs date-pill">
      <span class="dot"><svg width="12" height="12" viewBox="0 0 12 12"><rect x="1" y="2" width="10" height="9" rx="1.5" fill="none" stroke="#8dc21f" stroke-width="1.4"/><path d="M1 5h10M4 1v2M8 1v2" stroke="#8dc21f" stroke-width="1.4"/></svg></span>
      01 Nov 2023
    </div>
    <h1 class="abs cover-title">Environmental, Social, and Governance Report</h1>
    <p class="abs cover-sub">Consulting Business</p>
    <div class="abs illus cover-illus" role="img" aria-label="Flat illustration of business people working with laptops, charts and gears"></div>
  </section>

  <!-- Introduction -->
  <section class="slide">
    <h2 class="abs head-tab">Introduction</h2>
    <div class="abs client-mark head-mark">[client logo]</div>
    <p class="abs greet" style="left:60px; top:118px;">Dear reader,</p>
    <div class="abs copy" style="left:60px; top:155px; width:467px;">
      <p>We are pleased to present our annual ESG report, outlining our commitment and progress on key environmental, social and governance priorities. As a responsible business, we understand our obligation to consider our environmental and social impacts.</p>
      <p>This annual ESG report summarises our commitment to sustainability across our operations. Through data-driven insights, we have focused our strategy on material issues from carbon emissions to ethical conduct. While progress has been made, opportunities to improve remain.</p>
      <p>We will continue to embed responsible practices through collaboration with our stakeholders. Our aim is to drive long-term value creation by upholding the highest standards of integrity, championing diversity and inclusion, and supporting climate action. Though the road ahead is long, we are confident our collective efforts will build a resilient, equitable and sustainable future.</p>
    </div>
    <p class="abs sign" style="left:60px; top:470px;">ANNA LINDQVIST, <small>Consulting Business</small></p>
    <div class="abs illus" style="left:575px; top:145px; width:377px; height:315px;" role="img" aria-label="Flat illustration of a woman presenting a chart to a colleague seated at a desk"></div>
    <footer class="abs foot">
      <span class="cal"><svg width="13" height="13" viewBox="0 0 12 12"><rect x="1" y="2" width="10" height="9" rx="1.5" fill="none" stroke="#8dc21f" stroke-width="1.4"/><path d="M1 5h10M4 1v2M8 1v2" stroke="#8dc21f" stroke-width="1.4"/></svg></span>
      <span class="f-date">01 Nov 2023</span><span class="f-title">Environmental, Social, and Governance Report</span><span class="f-biz">Consulting Business</span><span class="f-page">Page No 02</span>
    </footer>
  </section>

  <!-- Frameworks -->
  <section class="slide">
    <h2 class="abs head-tab small">Relevant reporting frameworks</h2>
    <div class="abs client-mark head-mark">[client logo]</div>
    <div class="abs copy fine" style="left:60px; top:100px; width:467px;">
      <p>This report has been prepared in accordance with the latest versions of key voluntary ESG disclosure standards, including the EU Corporate Sustainability Reporting Directive (CSRD), the Carbon Ledger Protocol Corporate Standard and Corporate Value Chain Standard for greenhouse gas emissions, the Global Disclosure Initiative (GDI) Standards, the Climate Targets Alliance (CTA), and the Sector Materiality Standards Board (SMSB) Standards.</p>
      <p>By adhering to the newest versions of these major ESG frameworks, we aim to provide investors and stakeholders with consistent, comparable and reliable sustainability data based on the latest reporting requirements and recommendations.</p>
    </div>
    <ul class="abs bullets" style="left:60px; top:318px; width:467px;">
      <li><svg width="13" height="13" viewBox="0 0 13 13"><circle cx="6.5" cy="6.5" r="5.5" fill="none" stroke="#8dc21f" stroke-width="1.6"/><path d="M4 6.5h5M7 4.5l2 2-2 2" fill="none" stroke="#8dc21f" stroke-width="1.6"/></svg>EU Corporate Sustainability Reporting Directive (CSRD): The CSRD is an EU regulation that expands sustainability reporting requirements to a wider range of companies, introducing standardized reporting on environmental, social, and governance (ESG) topics to enhance transparency and comparability of corporate sustainability information.</li>
      <li><svg width="13" height="13" viewBox="0 0 13 13"><circle cx="6.5" cy="6.5" r="5.5" fill="none" stroke="#8dc21f" stroke-width="1.6"/><path d="M4 6.5h5M7 4.5l2 2-2 2" fill="none" stroke="#8dc21f" stroke-width="1.6"/></svg>Carbon Ledger Protocol Corporate Standard and Corporate Value Chain Standard for greenhouse gas emissions: These standards are internationally recognized guidelines that help companies measure and report their greenhouse gas emissions, with the Corporate Value Chain Standard focusing on emissions throughout a company's entire value chain.</li>
    </ul>
    <ul class="abs bullets" style="left:539px; top:102px; width:447px;">
      <li><svg width="13" height="13" viewBox="0 0 13 13"><circle cx="6.5" cy="6.5" r="5.5" fill="none" stroke="#8dc21f" stroke-width="1.6"/><path d="M4 6.5h5M7 4.5l2 2-2 2" fill="none" stroke="#8dc21f" stroke-width="1.6"/></svg>Global Disclosure Initiative (GDI) Standards: The GDI Standards are widely used global guidelines for reporting on sustainability topics, offering a comprehensive framework for organizations to disclose their economic, environmental, social, and governance performance.</li>
      <li><svg width="13" height="13" viewBox="0 0 13 13"><circle cx="6.5" cy="6.5" r="5.5" fill="none" stroke="#8dc21f" stroke-width="1.6"/><path d="M4 6.5h5M7 4.5l2 2-2 2" fill="none" stroke="#8dc21f" stroke-width="1.6"/></svg>Climate Targets Alliance (CTA): CTA is a collaborative effort to assist companies in setting and achieving ambitious science-based targets to reduce their carbon emissions in line with the goals of the Paris Agreement, helping combat climate change.</li>
      <li><svg width="13" height="13" viewBox="0 0 13 13"><circle cx="6.5" cy="6.5" r="5.5" fill="none" stroke="#8dc21f" stroke-width="1.6"/><path d="M4 6.5h5M7 4.5l2 2-2 2" fill="none" stroke="#8dc21f" stroke-width="1.6"/></svg>Sector Materiality Standards Board (SMSB) Standards: SMSB Standards provide industry-specific sustainability reporting guidelines, enabling companies to disclose financially material ESG information to investors, promoting better decision-making and risk assessment.</li>
    </ul>
    <div class="abs badges" role="img" aria-label="Badges of the reporting frameworks">
      <div class="badge"><i style="background:#f1c9c9"></i></div>
      <div class="badge"><i style="background:#c9d3ea"></i></div>
      <div class="badge"><i style="background:#cfe0ef"></i></div>
      <div class="badge"><i style="background:#e2e2e2"></i></div>
      <div class="badge"><i style="background:#263d96"></i></div>
      <div class="badge"><i style="background:#cde6f2"></i></div>
    </div>
    <div class="abs illus" style="left:750px; top:350px; width:220px; height:160px;" role="img" aria-label="Flat illustration of two people talking at a table among plants"></div>
    <footer class="abs foot">
      <span class="cal"><svg width="13" height="13" viewBox="0 0 12 12"><rect x="1" y="2" width="10" height="9" rx="1.5" fill="none" stroke="#8dc21f" stroke-width="1.4"/><path d="M1 5h10M4 1v2M8 1v2" stroke="#8dc21f" stroke-width="1.4"/></svg></span>
      <span class="f-date">01 Nov 2023</span><span class="f-title">Environmental, Social, and Governance Report</span><span class="f-biz">Consulting Business</span><span class="f-page">Page No 03</span>
    </footer>
  </section>

  <!-- Climate -->
  <section class="slide">
    <h2 class="abs head-tab">Climate</h2>
    <div class="abs client-mark head-mark">[client logo]</div>
    <div class="abs copy fine" style="left:60px; top:116px; width:467px;">
      <p>Addressing our contribution to climate change is a critical sustainability priority. This section outlines our greenhouse gas (GHG) emissions footprint across Scopes 1, 2, and 3, as well as our overall energy usage. We report this data to transparently manage our impacts, track reduction progress, and identify opportunities to transition to low-carbon operations through energy efficiency, renewable power, and other decarbonization initiatives.</p>
    </div>
    <p class="abs section-label" style="left:60px; top:250px;">CO<sub style="font-size:10px">2</sub> Emissions (Metric Tons)</p>
    <table class="abs scope-table">
      <tr><th>Scope 1</th><td>1.000.000</td></tr>
      <tr><th>Scope 2</th><td>0.000.009</td></tr>
      <tr><th>Scope 3</th><td>0.000.008</td></tr>
    </table>
    <p class="abs scope-note" style="left:60px; top:410px; width:467px;">Scope 1 covers direct emissions from burning fuels in company assets like vehicles, generators, boilers, and air conditioners. Scope 2 accounts for indirect emissions from purchased energy for heating, cooling, steam, and electricity. I.e. everything that can be found on the electricity and gas bill. Scope 3 includes other indirect emissions not in Scope 2, such as those from purchased goods and services, capital goods, transportation, distribution, and business travel.</p>
    <div class="abs copy fine" style="left:539px; top:116px; width:447px;">
      <p>Lorem ipsum dolor sit amet, consectetur adipiscing elit, sed do eiusmod tempor incididunt ut labore et dolore magna aliqua. Ut enim ad minim veniam, quis nostrud exercitation ullamco laboris nisi ut aliquip ex ea commodo consequat. Duis aute irure dolor in reprehenderit in voluptate velit esse cillum dolore eu fugiat nulla pariatur. Excepteur sint occaecat cupidatat non proident, sunt in culpa qui officia deserunt mollit anim id est laborum.</p>
    </div>
    <p class="abs section-label" style="left:539px; top:250px;">Energy Usage</p>
    <div class="abs stat" style="left:539px; top:279px;">
      <div class="ring"><b>0.999</b></div><p>Natural gas<br>(MWh)</p>
    </div>
    <div class="abs stat" style="left:734px; top:279px;">
      <div class="ring"><b>32%</b></div><p>% of total energy usage<br>from renewable sources</p>
    </div>
    <div class="abs illus" style="left:621px; top:370px; width:275px; height:120px;" role="img" aria-label="Flat illustration of a team at desks beside an energy-saving presentation board"></div>
    <footer class="abs foot">
      <span class="cal"><svg width="13" height="13" viewBox="0 0 12 12"><rect x="1" y="2" width="10" height="9" rx="1.5" fill="none" stroke="#8dc21f" stroke-width="1.4"/><path d="M1 5h10M4 1v2M8 1v2" stroke="#8dc21f" stroke-width="1.4"/></svg></span>
      <span class="f-date">01 Nov 2023</span><span class="f-title">Environmental, Social, and Governance Report</span><span class="f-biz">Consulting Business</span><span class="f-page">Page No 04</span>
    </footer>
  </section>

  <!-- Resources -->
  <section class="slide">
    <h2 class="abs head-tab">Resources</h2>
    <div class="abs client-mark head-mark">[client logo]</div>
    <div class="abs copy fine" style="left:60px; top:116px; width:467px;">
      <p>As a responsible business, we aim to sustainably manage our use of natural resources. This section details our water usage and circular economy efforts to minimize waste, increase recycling, and mitigate hazardous materials. We track this data to conserve resources, support circular systems, and reduce our environmental footprint across our operations and value chain. Our commitment to stewarding resources carefully considers relevant ecological impacts so we can uphold our social license to operate.</p>
    </div>
    <p class="abs section-label" style="left:60px; top:265px;">Water usage</p>
    <div class="abs stat" style="left:60px; top:296px;">
      <div class="ring"><b>0.111</b></div><p>m3 water from<br>municipal sources</p>
    </div>
    <div class="abs copy fine" style="left:60px; top:388px; width:467px;">
      <p>Lorem ipsum dolor sit amet, consectetur adipiscing elit, sed do eiusmod tempor incididunt ut labore et dolore magna aliqua. Ut enim ad minim veniam, quis nostrud exercitation ullamco laboris nisi ut aliquip ex ea commodo consequat. Duis aute irure dolor in reprehenderit in voluptate velit esse cillum dolore eu fugiat nulla pariatur. Excepteur sint occaecat cupidatat non proident, sunt in culpa qui officia deserunt mollit anim id est laborum.</p>
    </div>
    <p class="abs section-label" style="left:539px; top:122px;">Circularity</p>
    <div class="abs stat" style="left:539px; top:154px;">
      <div class="ring"><b>0.009</b></div><p>Metric tons of hazardous<br>waste</p>
    </div>
    <div class="abs stat" style="left:829px; top:154px;">
      <div class="ring"><b>68%</b></div><p>% recycled<br>materials</p>
    </div>
    <div class="abs illus" style="left:593px; top:240px; width:322px; height:252px;" role="img" aria-label="Flat illustration of people tending a growing money plant with a ladder"></div>
    <footer class="abs foot">
      <span class="cal"><svg width="13" height="13" viewBox="0 0 12 12"><rect x="1" y="2" width="10" height="9" rx="1.5" fill="none" stroke="#8dc21f" stroke-width="1.4"/><path d="M1 5h10M4 1v2M8 1v2" stroke="#8dc21f" stroke-width="1.4"/></svg></span>
      <span class="f-date">01 Nov 2023</span><span class="f-title">Environmental, Social, and Governance Report</span><span class="f-biz">Consulting Business</span><span class="f-page">Page No 05</span>
    </footer>
  </section>

  <!-- People -->
  <section class="slide">
    <h2 class="abs head-tab">People</h2>
    <div class="abs client-mark head-mark">[client logo]</div>
    <div class="abs copy fine" style="left:60px; top:116px; width:467px;">
      <p>Our employees are central to our identity and success as a business. This section outlines our commitment to foster a diverse, equitable workplace where all people feel valued, safe and empowered to reach their full potential. We report on demographics, inclusion initiatives, health and safety, training, and development programs. By tracking this data, we can cultivate talent, prevent risks, uphold ethical labor practices, and ensure our workforce thrives in an environment of belonging, care and purpose.</p>
    </div>
    <p class="abs section-label" style="left:60px; top:265px;">Key metrics</p>
    <table class="abs metric-table">
      <tr><th>% women and minorities on board and management team</th><td>1</td></tr>
      <tr><th>Gender pay gap ratio (men:women)</th><td>2</td></tr>
      <tr><th>Entry level wage to local living wage ratio</th><td>3</td></tr>
      <tr><th>Average number of training hours per employee</th><td>4</td></tr>
      <tr><th>Work-related fatalities/injuries at company sites</th><td>5</td></tr>
      <tr><th>% employees covered by collective bargaining agreement</th><td>6</td></tr>
    </table>
    <div class="abs copy fine" style="left:539px; top:116px; width:447px;">
      <p>Lorem ipsum dolor sit amet, consectetur adipiscing elit, sed do eiusmod tempor incididunt ut labore et dolore magna aliqua. Ut enim ad minim veniam, quis nostrud exercitation ullamco laboris nisi ut aliquip ex ea commodo consequat. Duis aute irure dolor in reprehenderit in voluptate velit esse cillum dolore eu fugiat nulla pariatur. Excepteur sint occaecat cupidatat non proident, sunt in culpa qui officia deserunt mollit anim id est in voluptate velit esse cillum dolore eu fugiat nulla derit in voluptate velit esse cillum dolore eu fugiat nulla orum.</p>
    </div>
    <div class="abs illus" style="left:564px; top:259px; width:393px; height:236px;" role="img" aria-label="Flat illustration of people leaving star ratings around a large tablet"></div>
    <footer class="abs foot">
      <span class="cal"><svg width="13" height="13" viewBox="0 0 12 12"><rect x="1" y="2" width="10" height="9" rx="1.5" fill="none" stroke="#8dc21f" stroke-width="1.4"/><path d="M1 5h10M4 1v2M8 1v2" stroke="#8dc21f" stroke-width="1.4"/></svg></span>
      <span class="f-date">01 Nov 2023</span><span class="f-title">Environmental, Social, and Governance Report</span><span class="f-biz">Consulting Business</span><span class="f-page">Page No 06</span>
    </footer>
  </section>

</main>
</body>
</html>
```